Fontenot Bayou Grillhouse (Owners Card)

Need a classy, but modern business card. I have included a promotional card for the steakhouse. I need one for myself (the owner) that is more professional.

Target Market(s)

General Public

Industry/Entity Type

Food service

Contact Information for Business Card

Name, business address, phone number, email, logo

Font styles to use
Serif
Sans Serif
Decorative
Script

Requirements
Must have
• My name (Darvel Pruitt), business address (327 Oakmere Street), phone number (510) 493-2615, email (Dpruittkr4@mailvane.example. On the back of the card: Psalms 27 1 The LORD is my light and my salvation— whom shall I fear? The LORD is the stronghold of my life— of whom shall I be afraid? 2 When the wicked advance against me to devour me, it is my enemies and my foes who will stumble and fall. 3 Though an army besiege me, my heart will not fear; though war break out against me, even then I will be confident.
Nice to have
• Something that’s bold, but modern and professional.

```html
<!DOCTYPE html>
<html lang="en">
<head>
<meta charset="utf-8">
<title>Fontenot Bayou Grillhouse — Owner Business Card</title>
<link rel="stylesheet" href="https://fonts.googleapis.com/css2?family=Inter:wght@400;500&family=Cormorant+SC:wght@500&display=swap">
<style>
  :root {
    --bg: #4d4d4d;
    --card: #000000;
    --ink: #ffffff;
    --label: #8a8a8a;
    --brand: #f5a623;
    --rule: #6b6b4a;
    --title-rule: #bdbdbd;
    --wine: #7a1a24;
    --red: #e8212b;
    --orange: #f7941d;
    --lime: #b5c934;
  }
  * { box-sizing: border-box; margin: 0; padding: 0; }
  html, body { width: 978px; height: 1200px; overflow: hidden; }
  body {
    background: var(--bg);
    font-family: "Inter", Arial, sans-serif;
    color: var(--ink);
    position: relative;
  }
  h1, h2 { font-weight: 400; font-size: inherit; }

  .side-label {
    position: absolute;
    top: 462px;
    font-family: "Cormorant SC", Georgia, serif;
    font-size: 11px;
    letter-spacing: 0.4px;
    color: var(--label);
  }
  .side-label--front { left: 54px; }
  .side-label--back { left: 529px; }

  .card {
    position: absolute;
    top: 500px;
    width: 411px;
    height: 235px;
    background: var(--card);
    overflow: hidden;
  }
  .card--front { left: 41px; }
  .card--back { left: 525px; }
  .card__waves { position: absolute; inset: 0; width: 100%; height: 100%; }

  .brand {
    position: absolute;
    display: flex;
    flex-direction: column;
    align-items: center;
    text-align: center;
    color: var(--brand);
    font-weight: 500;
  }
  .brand__dot { border-radius: 50%; background: var(--brand); }
  .card--front .brand { left: 14px; top: 72px; width: 180px; font-size: 17px; line-height: 1.15; }
  .card--front .brand__dot { width: 14px; height: 14px; margin-bottom: 8px; }
  .card--back .brand { left: 120px; top: 22px; width: 171px; font-size: 9px; line-height: 1.2; }
  .card--back .brand__dot { width: 9px; height: 9px; margin-bottom: 4px; }

  .divider {
    position: absolute;
    left: 201px; top: 69px;
    width: 1px; height: 104px;
    background: var(--rule);
  }
  .owner {
    position: absolute;
    left: 220px; top: 47px;
    font-size: 21px;
    line-height: 26px;
    padding-bottom: 2px;
    border-bottom: 1.5px solid var(--ink);
    letter-spacing: -0.2px;
  }
  .contacts { position: absolute; left: 220px; top: 91px; list-style: none; }
  .contacts li {
    display: flex; align-items: center;
    height: 26px;
    font-size: 11px;
  }
  .contacts svg { width: 7px; height: 8px; margin-right: 8px; flex: none; }

  .verse-title {
    position: absolute;
    left: 0; right: 0; top: 72px;
    text-align: center;
    font-size: 19px;
    line-height: 22px;
  }
  .verse-title span {
    display: inline-block;
    padding: 0 2px 3px;
    border-bottom: 1px solid var(--title-rule);
  }
  .verse {
    position: absolute;
    left: 0; right: 0; top: 104px;
    text-align: center;
    font-size: 10.3px;
    line-height: 13.5px;
    letter-spacing: -0.15px;
  }
  .verse p + p { margin-top: 5px; }
</style>
</head>
<body>
  <div class="side-label side-label--front">B card Front</div>
  <div class="side-label side-label--back">B card back</div>

  <section class="card card--front">
    <svg class="card__waves" viewBox="0 0 411 235" aria-hidden="true">
      <defs>
        <linearGradient id="waveTopF" x1="0" y1="0" x2="1" y2="0">
          <stop offset="0" stop-color="#7a1a24"/>
          <stop offset="0.35" stop-color="#e8212b"/>
          <stop offset="0.72" stop-color="#f7941d"/>
          <stop offset="1" stop-color="#b5c934"/>
        </linearGradient>
        <linearGradient id="waveBotF" x1="0" y1="0" x2="1" y2="0">
          <stop offset="0" stop-color="#b5c934"/>
          <stop offset="0.3" stop-color="#f7941d"/>
          <stop offset="0.65" stop-color="#e8212b"/>
          <stop offset="1" stop-color="#7a1a24"/>
        </linearGradient>
      </defs>
      <path d="M0 0 H144 C122 24 84 28 52 34 C28 39 10 45 0 53 Z" fill="url(#waveTopF)"/>
      <path d="M411 181 V235 H267 C282 220 305 213 335 208 C370 202 398 198 411 181 Z" fill="url(#waveBotF)"/>
    </svg>

    <div class="brand">
      <span class="brand__dot"></span>
      <span>Fontenot Bayou Grillhouse</span>
    </div>

    <div class="divider"></div>
    <h1 class="owner">Darvel Pruitt</h1>
    <ul class="contacts">
      <li>
        <svg viewBox="0 0 7 10" aria-hidden="true"><rect x="0.6" y="0.6" width="5.8" height="8.8" rx="1" fill="none" stroke="#fff" stroke-width="1.1"/><rect x="2.5" y="7.6" width="2" height="0.8" fill="#fff"/></svg>
        (510) 493-2615
      </li>
      <li>
        <svg viewBox="0 0 7 10" aria-hidden="true"><circle cx="3.5" cy="3.3" r="2.4" fill="none" stroke="#fff" stroke-width="1.1"/><path d="M0.5 9.4 H6.5" stroke="#fff" stroke-width="1.1"/></svg>
        327 Oakmere Street
      </li>
      <li>
        <svg viewBox="0 0 8 6" aria-hidden="true"><rect width="8" height="6" fill="#fff"/><path d="M0 0 L4 3.4 L8 0" fill="none" stroke="#000" stroke-width="0.8"/></svg>
        Dpruittkr4@mailvane.example
      </li>
    </ul>
  </section>

  <section class="card card--back">
    <svg class="card__waves" viewBox="0 0 411 235" aria-hidden="true">
      <defs>
        <linearGradient id="waveTopB" x1="0" y1="0" x2="1" y2="0">
          <stop offset="0" stop-color="#7a1a24"/>
          <stop offset="0.35" stop-color="#e8212b"/>
          <stop offset="0.72" stop-color="#f7941d"/>
          <stop offset="1" stop-color="#b5c934"/>
        </linearGradient>
        <linearGradient id="waveBotB" x1="0" y1="0" x2="1" y2="0">
          <stop offset="0" stop-color="#b5c934"/>
          <stop offset="0.3" stop-color="#f7941d"/>
          <stop offset="0.65" stop-color="#e8212b"/>
          <stop offset="1" stop-color="#7a1a24"/>
        </linearGradient>
      </defs>
      <path d="M0 0 H144 C122 24 84 28 52 34 C28 39 10 45 0 53 Z" fill="url(#waveTopB)"/>
      <path d="M411 181 V235 H267 C282 220 305 213 335 208 C370 202 398 198 411 181 Z" fill="url(#waveBotB)"/>
    </svg>

    <div class="brand">
      <span class="brand__dot"></span>
      <span>Fontenot Bayou Grillhouse</span>
    </div>

    <h2 class="verse-title"><span>Psalms 27</span></h2>
    <div class="verse">
      <p>The LORD is my light and my salvation— whom shall I fear?<br>The LORD is the stronghold of my life— of whom shall I be afraid?</p>
      <p>When the wicked advance against me to devour me,<br>it is my enemies and my foes who will stumble and fall.</p>
      <p>Though an army besiege me, my heart will not fear;<br>though war break out against me, even then I will be confident.</p>
    </div>
  </section>
</body>
</html>
```